RBAL High Performance Presentation Deck

RBAL is an Nationally recognized Junior Tennis Training Facility located in College Park, MD. We are considered to be experts in the field of Junior Tennis development. RBAL is a 501c3 that has an extensive Community Outreach arm that delivers tennis and education opportunities to underserved communities around Washington D.C. and Prince Georges County MD. We provide financial aid in the form of program scholarships to anyone qualifying for assistance. To date RBAL Students have recived more than $21M in college scholarships. The attached file is used when presenting to potential business partners for the purposes of partnering our programs, consulting work, or management agreements. We need to have the attached file cleaned up, condensed down to less than 20 pages, given a fresh look and converted to a workable document

Target Market(s)

Business to Business Partners, Those seeking information about partnering with us for business oportunities

Font styles to use
Serif

Colors
0455a3
9bcb3c
ffffff

Requirements
Must have
• Color palette: PMS 293, CMYK 100. 57.0. 2
PMS 382 CMYK 29.0.100.0
Logos. Most of the information contained in the attachment. Bios can be cut down significantly. Other information can bb made more concise.
Needs to be less than 20 pages
Nice to have
• a more modern look
less than 16 pages

```html
<!DOCTYPE html>
<html lang="en">
<head>
<meta charset="utf-8">
<title>RBAL High Performance Deck – Senior Staff</title>
<link href="https://fonts.googleapis.com/css2?family=Roboto:wght@400;500;700&display=swap" rel="stylesheet">
<style>
:root{
  --blue:#0455a3;
  --navy:#1a4a9c;
  --green:#9bcb3c;
  --white:#ffffff;
  --text:#4a4a4a;
  --backdrop:#e4e4e4;
}
*{margin:0;padding:0;box-sizing:border-box}
html,body{width:1200px;height:691px;overflow:hidden}
body{background:var(--backdrop);font-family:"Roboto",Arial,sans-serif;position:relative;color:var(--text)}
.page{position:absolute;top:94px;width:355px;height:502px;background:var(--white);overflow:hidden}
.page--left{left:232px}
.page--right{left:614px}
.corner-block{position:absolute;right:0;top:0;width:22px;height:22px;background:var(--blue)}
.brand{position:absolute;left:19px;top:18px;font-weight:500;font-size:16px;color:var(--navy);line-height:1}
.brand-rule{position:absolute;left:100px;right:0;top:26px;height:2.5px;background:var(--green)}
.section-title{position:absolute;font-weight:700;font-size:8.3px;color:var(--navy);line-height:1;white-space:nowrap}
.section-title::after{content:"";position:absolute;left:0;right:0;top:13px;height:1.5px;background:var(--green)}
.staff{position:absolute;width:159px}
.staff__photo{position:absolute;left:0;top:0;width:32px;height:32px;border-radius:50%;background:var(--green)}
.staff__name{position:absolute;left:37px;top:-2px;font-size:7.8px;color:var(--navy);font-weight:400;white-space:nowrap}
.staff__role{position:absolute;left:37px;top:10px;height:5.5px;width:121px;background:var(--green);color:var(--white);font-size:3.1px;font-weight:700;letter-spacing:1.1px;text-transform:uppercase;line-height:5.5px;padding-left:2px;white-space:nowrap;overflow:hidden}
.staff__role--short{width:99px}
.staff__email{position:absolute;left:37px;top:18px;display:flex;align-items:center;gap:3px;font-size:5.6px;color:var(--navy)}
.staff__email svg{width:9px;height:6px}
.staff__bio{position:absolute;left:0;top:40px;width:159px;font-size:4.75px;line-height:6px;text-align:justify;color:var(--text)}
.coaches-intro{position:absolute;left:14px;top:241px;width:160px;font-size:4.6px;line-height:5.8px;color:var(--text)}
.coach{position:absolute;width:56px;text-align:center}
.coach__photo{width:30px;height:30px;border-radius:50%;background:var(--green);margin:0 auto}
.coach__name{margin-top:7px;font-size:5.8px;color:var(--navy);font-weight:400;white-space:nowrap}
.coach__role{margin:3px auto 0;height:5px;width:38px;background:var(--green);color:var(--white);font-size:2.9px;font-weight:700;letter-spacing:.9px;line-height:5px;text-transform:uppercase;white-space:nowrap;overflow:hidden}
.coach__desc{margin-top:5px;font-size:4.1px;line-height:5.4px;color:var(--text)}
.tech-name{position:absolute;left:290px;top:57px;font-size:10px;font-weight:500;color:var(--navy);line-height:1}
.tech-visual{position:absolute;left:186px;top:82px;width:169px;height:96px;background:linear-gradient(135deg,#3a2c7a 0%,#2d4fa8 45%,#2f8f7a 80%,#57b04a 100%)}
.tech-panel{position:absolute;left:186px;top:178px;width:169px;height:101px;background:var(--navy);color:var(--white);font-size:5.9px;line-height:8.35px;text-align:justify;padding:6px 9px 0 9px}
.tech-photo{position:absolute;left:186px;top:279px;width:169px;height:96px;background:linear-gradient(180deg,#5e7a5a 0%,#3f4f45 45%,#7a2c34 100%)}
.tech-features{position:absolute;left:186px;top:375px;width:169px;height:80px;background:var(--green);text-align:center;color:var(--navy);padding-top:8px}
.tech-features__title{font-size:7.8px;font-weight:400;margin-bottom:4px}
.tech-features ul{list-style:none;font-size:5.7px;line-height:8.4px}
.page-number{position:absolute;top:479px;font-size:5.6px;font-weight:700;color:var(--navy)}
.page-band{position:absolute;left:0;right:0;bottom:0;height:5px;background:var(--blue)}
</style>
</head>
<body>

<section class="page page--left">
  <div class="corner-block"></div>
  <div class="brand">RBAL</div>
  <div class="brand-rule"></div>
  <h2 class="section-title" style="left:20px;top:55px">Meet our Senior Staff</h2>

  <article class="staff" style="left:14px;top:82px">
    <div class="staff__photo"></div>
    <h3 class="staff__name">Idris Okonkwo</h3>
    <div class="staff__role">Senior Director of Junior Champions</div>
    <div class="staff__email"><svg viewBox="0 0 9 6"><rect width="9" height="6" fill="#1a4a9c"/><path d="M0 0L4.5 3.3L9 0M0 6L3.3 2.5M9 6L5.7 2.5" stroke="#fff" stroke-width=".7" fill="none"/></svg>iokonkwo@rbal.org</div>
    <p class="staff__bio">Idris leads the junior champions program and has guided players of every level through the full development pathway. A founding member of the coaching staff, he has shaped the training of many national champions, college athletes and touring professionals. Before joining the academy he competed internationally and served as a practice partner on the professional tour. He has mentored top ranked juniors through major junior titles and deep runs at international events. He also represented his country in team competition and at the highest level of the sport. His greatest pride is helping young athletes grow on and off the court through discipline, joy and hard work. He holds high performance certifications from the leading coaching bodies and keeps learning every season.</p>
  </article>

  <article class="staff" style="left:182px;top:82px">
    <div class="staff__photo"></div>
    <h3 class="staff__name">Lena Varga</h3>
    <div class="staff__role">Senior Director of Junior Champions</div>
    <div class="staff__email"><svg viewBox="0 0 9 6"><rect width="9" height="6" fill="#1a4a9c"/><path d="M0 0L4.5 3.3L9 0M0 6L3.3 2.5M9 6L5.7 2.5" stroke="#fff" stroke-width=".7" fill="none"/></svg>iokonkwo@rbal.org</div>
    <p class="staff__bio">Idris leads the junior champions program and has guided players of every level through the full development pathway. A founding member of the coaching staff, he has shaped the training of many national champions, college athletes and touring professionals. Before joining the academy he competed internationally and served as a practice partner on the professional tour. He has mentored top ranked juniors through major junior titles and deep runs at international events. He also represented his country in team competition and at the highest level of the sport. His greatest pride is helping young athletes grow on and off the court through discipline, joy and hard work. He holds high performance certifications from the leading coaching bodies and keeps learning every season.</p>
  </article>

  <article class="staff" style="left:14px;top:210px">
    <div class="staff__photo"></div>
    <h3 class="staff__name">Tomas Adeyemi</h3>
    <div class="staff__role staff__role--short">Senior Director of Champions</div>
    <div class="staff__email"><svg viewBox="0 0 9 6"><rect width="9" height="6" fill="#1a4a9c"/><path d="M0 0L4.5 3.3L9 0M0 6L3.3 2.5M9 6L5.7 2.5" stroke="#fff" stroke-width=".7" fill="none"/></svg>tadeyemi@rbal.org</div>
    <p class="staff__bio">Tomas is a ten year veteran of the professional tour. During his playing career he reached the later rounds of every major event, earned a top fifty doubles ranking and won several doubles titles on the international circuit. He also reached a career high singles ranking and won a singles title on the challenger circuit. Before turning professional he graduated from a respected university with a degree in sociology, where he set the school record for combined singles and doubles wins and earned top national rankings. He was a six time all conference selection and a national championship finalist. He has received awards for leadership and sportsmanship and has served in coaching roles for touring players, including a major champion. As general manager he brings a wealth of experience to the player development programs and to every family in the academy. He is a certified teaching professional.</p>
  </article>

  <article class="staff" style="left:182px;top:210px">
    <div class="staff__photo"></div>
    <h3 class="staff__name">Noor Halvorsen</h3>
    <div class="staff__role staff__role--short">Senior Director of Champions</div>
    <div class="staff__email"><svg viewBox="0 0 9 6"><rect width="9" height="6" fill="#1a4a9c"/><path d="M0 0L4.5 3.3L9 0M0 6L3.3 2.5M9 6L5.7 2.5" stroke="#fff" stroke-width=".7" fill="none"/></svg>tadeyemi@rbal.org</div>
    <p class="staff__bio">Tomas is a ten year veteran of the professional tour. During his playing career he reached the later rounds of every major event, earned a top fifty doubles ranking and won several doubles titles on the international circuit. He also reached a career high singles ranking and won a singles title on the challenger circuit. Before turning professional he graduated from a respected university with a degree in sociology, where he set the school record for combined singles and doubles wins and earned top national rankings. He was a six time all conference selection and a national championship finalist. He has received awards for leadership and sportsmanship and has served in coaching roles for touring players, including a major champion. As general manager he brings a wealth of experience to the player development programs and to every family in the academy. He is a certified teaching professional.</p>
  </article>

  <article class="staff" style="left:14px;top:361px">
    <div class="staff__photo"></div>
    <h3 class="staff__name">Eitan Morel</h3>
    <div class="staff__role staff__role--short">Director of High Performance</div>
    <div class="staff__email"><svg viewBox="0 0 9 6"><rect width="9" height="6" fill="#1a4a9c"/><path d="M0 0L4.5 3.3L9 0M0 6L3.3 2.5M9 6L5.7 2.5" stroke="#fff" stroke-width=".7" fill="none"/></svg>emorel@rbal.org</div>
    <p class="staff__bio">Eitan oversees the high performance champions program. Most of the players in this group train as full time student athletes. Before joining the academy he served as a national junior coach, youth olympic coach and team cup assistant for his home country. During his long career he has mentored top ranked professional players, leading international juniors and a number one ranked under fourteen player. He holds advanced certifications from the leading international coaching bodies. He was a top ranked junior player before completing his national service at the age of eighteen. He is a certified teaching professional who loves building complete competitors.</p>
  </article>

  <article class="staff" style="left:182px;top:361px">
    <div class="staff__photo"></div>
    <h3 class="staff__name">RJ Danforth</h3>
    <div class="staff__role staff__role--short">Director of High Performance</div>
    <div class="staff__email"><svg viewBox="0 0 9 6"><rect width="9" height="6" fill="#1a4a9c"/><path d="M0 0L4.5 3.3L9 0M0 6L3.3 2.5M9 6L5.7 2.5" stroke="#fff" stroke-width=".7" fill="none"/></svg>emorel@rbal.org</div>
    <p class="staff__bio">Eitan oversees the high performance champions program. Most of the players in this group train as full time student athletes. Before joining the academy he served as a national junior coach, youth olympic coach and team cup assistant for his home country. During his long career he has mentored top ranked professional players, leading international juniors and a number one ranked under fourteen player. He holds advanced certifications from the leading international coaching bodies. He was a top ranked junior player before completing his national service at the age of eighteen. He is a certified teaching professional who loves building complete competitors.</p>
  </article>

  <div class="page-number" style="left:174px">06</div>
  <div class="page-band"></div>
</section>

<section class="page page--right">
  <div class="corner-block"></div>
  <div class="brand">RBAL</div>
  <div class="brand-rule"></div>
  <h2 class="section-title" style="left:20px;top:55px">Meet our Senior Staff</h2>

  <article class="staff" style="left:14px;top:82px">
    <div class="staff__photo"></div>
    <h3 class="staff__name">Owen Park</h3>
    <div class="staff__role">Senior Director of Junior Champions</div>
    <div class="staff__email"><svg viewBox="0 0 9 6"><rect width="9" height="6" fill="#1a4a9c"/><path d="M0 0L4.5 3.3L9 0M0 6L3.3 2.5M9 6L5.7 2.5" stroke="#fff" stroke-width=".7" fill="none"/></svg>iokonkwo@rbal.org</div>
    <p class="staff__bio">Idris leads the junior champions program and has guided players of every level through the full development pathway. A founding member of the coaching staff, he has shaped the training of many national champions, college athletes and touring professionals. Before joining the academy he competed internationally and served as a practice partner on the professional tour. He has mentored top ranked juniors through major junior titles and deep runs at international events. He also represented his country in team competition and at the highest level of the sport. His greatest pride is helping young athletes grow on and off the court through discipline, joy and hard work. He holds high performance certifications from the leading coaching bodies and keeps learning every season.</p>
  </article>

  <h2 class="section-title" style="left:20px;top:216px">Additional Staff Coaches &amp; Experts</h2>
  <p class="coaches-intro">RBAL Senior Staff is complemented by the following coaches and experts who provide year-round support to RBAL's juniors and members.</p>

  <div class="coach" style="left:8px;top:260px"><div class="coach__photo"></div><div class="coach__name">Marcus Hale</div><div class="coach__role">Co-Director</div><div class="coach__desc">Director of the Champs<br>II Program</div></div>
  <div class="coach" style="left:64px;top:260px"><div class="coach__photo"></div><div class="coach__name">Grant Ellison</div><div class="coach__role">Co-Director</div><div class="coach__desc">Director of the Champs<br>II Program</div></div>
  <div class="coach" style="left:121px;top:260px"><div class="coach__photo"></div><div class="coach__name">Delia Monroe</div><div class="coach__role">Coach</div><div class="coach__desc">Tennis Coach for the<br>Champs I and II<br>programs</div></div>
  <div class="coach" style="left:8px;top:347px"><div class="coach__photo"></div><div class="coach__name">Rosa Ibarra</div><div class="coach__role">Coach/Apparel Rep</div><div class="coach__desc">Tennis Coach and RBAL<br>Apparel Representative</div></div>
  <div class="coach" style="left:64px;top:347px"><div class="coach__photo"></div><div class="coach__name">Helen Ashby</div><div class="coach__role">Mental Health</div><div class="coach__desc">Mental Conditioning and<br>Nutritional Advisor</div></div>
  <div class="coach" style="left:121px;top:347px"><div class="coach__photo"></div><div class="coach__name">Aleksi Varto</div><div class="coach__role">Fitness</div><div class="coach__desc">Physical Fitness and<br>Flexibility Coach</div></div>

  <h2 class="section-title" style="left:186px;top:55px">Court Technology</h2>
  <div class="tech-name">CourtView</div>
  <div class="tech-visual" role="img" aria-label="Illustration of an indoor tennis court with camera tracking and score display"></div>
  <p class="tech-panel">Four of RBAL's fifteen indoor tennis courts are equipped with CourtView technology. CourtView is engineered to provide state of the art tennis analytics through video and audio resources. CourtView's value is widely embraced by the tennis community, from recreational players to touring professionals. The technology is also widely used by college tennis programs, offering live video streams of college matches to a broad audience. RBAL is proud to be an original partner of CourtView, and continues to use the technology as a part of its junior training.</p>
  <div class="tech-photo" role="img" aria-label="Photo of junior players gathered around a court-side video screen"></div>
  <div class="tech-features">
    <h3 class="tech-features__title">On-Court Technology</h3>
    <ul>
      <li>Multi-dimensional video</li>
      <li>Instant feedback</li>
      <li>Limitless drill creation and storage</li>
      <li>Live ball calling</li>
      <li>Audio feedback for drill completion</li>
      <li>Video replay for fair play</li>
    </ul>
  </div>

  <div class="page-number" style="left:174px">07</div>
  <div class="page-band"></div>
</section>

</body>
</html>
```